Dental care for hole family, announcement in newspaper

Hey! I have Dental surgery Business in middle of Finland in Jyväskylä. You can see my web www.hammasvelmora.fi.
Now I am looking for new way to do advertisement, more visual I hope.
I woul like to have announcement in newspaper. I would like to tell that we treating hole family from babyes to seniors. I saw here in your pages cute photo where about 1-year old baby was brushing teeth ja looking with big eys to me. It is the feeling I am looking for. My idea is to tell people, that in our klinik, they can have "own dental hygienist" who is taking care of them with dentists of different spesialitis.
Now I need advertisements for that information!!

Yours, Velmora

Target Market(s)

All.

Industry/Entity Type

Dental Clinic

Requirements
Must have
• Visual components, whicts are matching with my homepages visual look (www.hammasvelmora.fi).
Nice to have
• My logo, whitch you can find from my webpages.

```html
<!DOCTYPE html>
<html lang="en">
<head>
<meta charset="utf-8">
<title>Hammasvelmora – Get the smile you deserve</title>
<link href="https://fonts.googleapis.com/css2?family=Crimson+Pro:ital,wght@0,400;0,600;0,700;0,800;1,400&display=swap" rel="stylesheet">
<style>
  :root {
    --brown: #8a5e33;
    --ink: #111;
    --body: #3d3d3d;
    --tick: #1f6ea6;
    --paper: #fff;
  }
  * { box-sizing: border-box; margin: 0; padding: 0; }
  html, body { width: 1200px; height: 833px; overflow: hidden; background: var(--paper); }
  .ad {
    position: relative; width: 1200px; height: 833px; overflow: hidden;
    font-family: "Crimson Pro", Georgia, serif; color: var(--ink); background: var(--paper);
  }
  .hero { position: absolute; left: 0; top: 0; width: 1200px; height: 400px; }
  .headline { font-family: "Crimson Pro", Georgia, serif; font-weight: 800; font-size: 104px; fill: var(--ink); }
  .tagline { font-family: "Crimson Pro", Georgia, serif; font-weight: 700; font-size: 44px; fill: #fff; }
  .intro {
    position: absolute; left: 84px; top: 440px; width: 700px;
    font-style: italic; font-size: 22.5px; line-height: 28px; text-align: center; color: var(--body);
  }
  .contact-box {
    position: absolute; left: 36px; top: 656px; width: 798px; height: 158px;
    border: 2px solid var(--ink);
  }
  .contact-box__invite {
    position: absolute; left: 46px; top: 50px;
    font-weight: 700; font-size: 21.5px; line-height: 35px;
  }
  .contact-box__details { position: absolute; left: 480px; top: 6px; width: 330px; text-align: center; }
  .contact-box__lead { font-size: 27px; line-height: 32px; }
  .contact-box__phone { font-weight: 700; font-size: 56px; line-height: 52px; color: var(--brown); letter-spacing: 1px; }
  .contact-box__web { font-weight: 700; font-size: 23px; line-height: 28px; color: var(--brown); }
  .contact-box__email { font-size: 20px; line-height: 26px; }
  .services { position: absolute; left: 888px; top: 378px; list-style: none; }
  .services__item {
    position: relative; padding-left: 38px; margin-bottom: 12px;
    font-weight: 700; font-size: 23.5px; line-height: 28px;
  }
  .services__item svg { position: absolute; left: 0; top: 6px; width: 22px; height: 20px; }
  .brand {
    position: absolute; right: 30px; top: 760px;
    display: flex; align-items: center; gap: 10px;
    font-weight: 700; font-size: 32px; line-height: 38px; color: var(--brown);
  }
  .brand__dot { width: 14px; height: 14px; border-radius: 50%; background: var(--brown); }
</style>
</head>
<body>
<main class="ad">
  <svg class="hero" viewBox="0 0 1200 400" xmlns="http://www.w3.org/2000/svg">
    <defs>
      <linearGradient id="smileTone" x1="0" y1="0" x2="1" y2="1">
        <stop offset="0" stop-color="#f3d6cc"/>
        <stop offset=".5" stop-color="#e7a9a2"/>
        <stop offset="1" stop-color="#f6ece8"/>
      </linearGradient>
      <path id="bandLine" d="M414,366 Q800,326 1190,166"/>
    </defs>
    <rect class="hero__photo" x="0" y="0" width="450" height="316" fill="url(#smileTone)" role="img" aria-label="Close-up photo of a smiling mouth with white teeth"/>
    <path class="hero__band" d="M0,304 Q560,404 1200,120 L1200,190 Q620,494 0,316 Z" fill="var(--brown)"/>
    <text class="headline" transform="translate(466,170) rotate(-9)" textLength="568" lengthAdjust="spacingAndGlyphs">Get the smile</text>
    <text class="headline" transform="translate(474,262) rotate(-11)" textLength="578" lengthAdjust="spacingAndGlyphs">you deserve!</text>
    <text class="tagline"><textPath href="#bandLine" textLength="770" lengthAdjust="spacingAndGlyphs">A Healthier Smile For a Healthier You</textPath></text>
  </svg>

  <p class="intro">We care for the whole family, from babies to seniors. With 90% of dental diseases having few symptoms till advanced stages, a comprehensive examination is imperative. In our clinic you have your own dental hygienist, working together with dentists of different specialities. As we make your teeth and gums healthier, the result is often an improvement in your smile.</p>

  <section class="contact-box">
    <p class="contact-box__invite">Schedule an appointment with us for<br>a comprehensive dental consultation.</p>
    <div class="contact-box__details">
      <p class="contact-box__lead">Call us today on</p>
      <p class="contact-box__phone">014 555 019</p>
      <p class="contact-box__web">www.hammasvelmora.fi</p>
      <p class="contact-box__email">hammasvelmora@lumoterveys.fi</p>
    </div>
  </section>

  <ul class="services">
    <li class="services__item"><svg viewBox="0 0 22 20"><path d="M2,11 L8,17 L20,2" fill="none" stroke="var(--tick)" stroke-width="3.5" stroke-linecap="round"/></svg>Preventive Dentistry</li>
    <li class="services__item"><svg viewBox="0 0 22 20"><path d="M2,11 L8,17 L20,2" fill="none" stroke="var(--tick)" stroke-width="3.5" stroke-linecap="round"/></svg>Family Dentistry</li>
    <li class="services__item"><svg viewBox="0 0 22 20"><path d="M2,11 L8,17 L20,2" fill="none" stroke="var(--tick)" stroke-width="3.5" stroke-linecap="round"/></svg>Implant and<br>Restorative Dentistry</li>
    <li class="services__item"><svg viewBox="0 0 22 20"><path d="M2,11 L8,17 L20,2" fill="none" stroke="var(--tick)" stroke-width="3.5" stroke-linecap="round"/></svg>Orthodontics</li>
    <li class="services__item"><svg viewBox="0 0 22 20"><path d="M2,11 L8,17 L20,2" fill="none" stroke="var(--tick)" stroke-width="3.5" stroke-linecap="round"/></svg>Braces/Clearline/ Arcfit</li>
    <li class="services__item"><svg viewBox="0 0 22 20"><path d="M2,11 L8,17 L20,2" fill="none" stroke="var(--tick)" stroke-width="3.5" stroke-linecap="round"/></svg>Aligner</li>
    <li class="services__item"><svg viewBox="0 0 22 20"><path d="M2,11 L8,17 L20,2" fill="none" stroke="var(--tick)" stroke-width="3.5" stroke-linecap="round"/></svg>Cosmetic Dentistry</li>
    <li class="services__item"><svg viewBox="0 0 22 20"><path d="M2,11 L8,17 L20,2" fill="none" stroke="var(--tick)" stroke-width="3.5" stroke-linecap="round"/></svg>Children Dentistry</li>
  </ul>

  <div class="brand">
    <span class="brand__dot"></span>
    <span class="brand__name">Hammasvelmora</span>
  </div>
</main>
</body>
</html>
```